Rise As Captain Book Cover Design

Book Cover Design Brief
Book Title
Rise As Captain
Subtitle
The 10 Quiet Habits of Remarkable Command
Author
Orwen Dalquist
Overview
This book is about leadership that starts within.
Most leadership books focus on tactics or management strategies. This book focuses on the inner disciplines that create powerful leaders — mindset, integrity, focus, empathy, professionalism, honesty, and self-respect.
The tone of the book is bold, direct, confident, and transformational.
This is not a soft or corporate leadership book. It is a call to step up and become the leader you are capable of becoming.
The cover should feel:
• Powerful
• Professional
• Transformational
• Premium
• Memorable
Think best-selling leadership book, not a generic business book.
Target Audience
Business owners
Managers
Entrepreneurs
Team leaders
Professionals who want to grow as leaders
Most readers are ambitious professionals who want to level up their leadership and life.
Design Direction
The design should communicate:
Strength. Discipline. Leadership. Personal transformation.
Avoid cliché leadership visuals like:
• Handshakes
• Office buildings
• Corporate stock imagery
• Teams sitting around tables
The design should feel iconic, bold, and timeless.
Think about covers of successful leadership books such as:
Copper Rituals
Total Stewardship
Won't Break Now
Begin From Purpose
The 36 Rules of Sway
These covers are simple, powerful, and recognizable even at small sizes.
Typography
The title RISE AS CAPTAIN should be:
• Bold
• Strong
• Dominant on the cover
• Easy to read even at small sizes (important for Vellora thumbnails)
The subtitle should be clean and secondary to the title.
The overall typography should feel strong, modern, and premium.
Color Direction
Designers are free to explore colors, but the cover should feel strong and premium, not playful.
Colors that often work well for leadership books include:
Black
Gold
White
Deep blue
Dark red
High contrast and clarity are important.
Style
Preferred style:
• Clean
• Modern
• Minimal
• Strong contrast
Avoid clutter and overly busy designs.
The goal is to create a cover that feels powerful and professional at first glance.
Deliverables
Front cover design for a leadership book.
Final files should include:
• High resolution artwork
• Editable source files
• Print-ready version suitable for publishing
Goal of the Cover
When someone sees this book on Vellora or in a bookstore, they should immediately think:
“This looks like a serious leadership book.”
The design should feel like it belongs next to books by authors such as:
Marcus Thorley
Brandt Osgood
Peter Hollis
Nolan Fairbrook
A strong, confident cover that attracts leaders who want to grow and perform at a higher level.
Target Market(s)
Business Owners and High level managers
Look and feel
Each slider illustrates characteristics of the customer's brand and the style your logo design should communicate.

```html
<!DOCTYPE html>
<html lang="en">
<head>
<meta charset="utf-8">
<title>Rise As Captain — Book Cover</title>
<link rel="stylesheet" href="https://fonts.googleapis.com/css2?family=Saira+Extra+Condensed:wght@500;600;700&display=swap">
<style>
  :root {
    --backdrop: #efefef;
    --cover-black: #000000;
    --gold-deep: #cf9d4e;
    --gold-light: #fbe9a6;
    --subtitle-white: #ffffff;
    --author-ink: #0a0a0a;
  }
  html, body {
    margin: 0;
    padding: 0;
    width: 1200px;
    height: 1200px;
    overflow: hidden;
    background: var(--backdrop);
  }
  .book-cover {
    position: absolute;
    left: 265px;
    top: 98px;
    width: 668px;
    height: 1002px;
    background: var(--cover-black);
    overflow: hidden;
  }
  .book-cover svg {
    display: block;
    width: 668px;
    height: 1002px;
  }
  .title-line {
    font-family: "Saira Extra Condensed", "Arial Narrow", sans-serif;
    font-weight: 600;
    font-size: 296px;
    fill: url(#goldSweep);
  }
  .subtitle-line {
    font-family: "Saira Extra Condensed", "Arial Narrow", sans-serif;
    font-weight: 600;
    font-size: 52px;
    fill: var(--subtitle-white);
  }
  .author-name {
    font-family: "Saira Extra Condensed", "Arial Narrow", sans-serif;
    font-weight: 700;
    font-size: 62px;
    fill: var(--author-ink);
  }
</style>
</head>
<body>
  <div class="book-cover">
    <svg viewBox="0 0 668 1002" xmlns="http://www.w3.org/2000/svg">
      <defs>
        <linearGradient id="goldSweep" gradientUnits="userSpaceOnUse" x1="150" y1="0" x2="640" y2="0">
          <stop offset="0" stop-color="#cf9d4e"/>
          <stop offset="0.5" stop-color="#fbe9a6"/>
          <stop offset="1" stop-color="#cf9d4e"/>
        </linearGradient>
        <linearGradient id="bandSweep" gradientUnits="userSpaceOnUse" x1="208" y1="0" x2="668" y2="0">
          <stop offset="0" stop-color="#c9954a"/>
          <stop offset="0.4" stop-color="#fbe9a6"/>
          <stop offset="1" stop-color="#cf9d4e"/>
        </linearGradient>
        <linearGradient id="heroTone" x1="0" y1="0" x2="1" y2="0">
          <stop offset="0" stop-color="#8a5a1c"/>
          <stop offset="0.5" stop-color="#e9c066"/>
          <stop offset="1" stop-color="#a8752a"/>
        </linearGradient>
      </defs>

      <!-- hero image area -->
      <rect class="hero-image" x="0" y="0" width="130" height="1002" fill="url(#heroTone)"
            role="img" aria-label="Golden chess king piece standing along the left edge of the cover"/>

      <!-- author band -->
      <rect class="author-band" x="208" y="902" width="460" height="55" fill="url(#bandSweep)"/>
      <text class="author-name" x="235" y="946" textLength="290" lengthAdjust="spacingAndGlyphs">ORWEN DALQUIST</text>

      <!-- title -->
      <text class="title-line" x="162" y="349" textLength="250" lengthAdjust="spacingAndGlyphs">RISE</text>
      <text class="title-line" x="158" y="582" textLength="175" lengthAdjust="spacingAndGlyphs">AS</text>
      <text class="title-line" x="162" y="812" textLength="465" lengthAdjust="spacingAndGlyphs">CAPTAIN</text>

      <!-- subtitle -->
      <text class="subtitle-line" x="400" y="409" textLength="205" lengthAdjust="spacingAndGlyphs">THE 10 QUIET</text>
      <text class="subtitle-line" x="400" y="467" textLength="160" lengthAdjust="spacingAndGlyphs">HABITS OF</text>
      <text class="subtitle-line" x="400" y="525" textLength="200" lengthAdjust="spacingAndGlyphs">REMARKABLE</text>
      <text class="subtitle-line" x="400" y="582" textLength="165" lengthAdjust="spacingAndGlyphs">COMMAND</text>
    </svg>
  </div>
</body>
</html>
```